I have working web app created using PHP + MySQL, but design is very bad. I need great designer to transform this in best mosque screen display app.

Example:
https://mytalvenor.com/products/ru-denkor
https://apps.brovanta.com/store/apps/details?id=com.pelorin.screen&hl=en_US&pli=1

We will run using Android TV

```html
<!DOCTYPE html>
<html lang="en">
<head>
<meta charset="utf-8">
<title>Login</title>
<link rel="stylesheet" href="https://fonts.googleapis.com/css2?family=Montserrat:wght@700;800&family=Inter:wght@400;500&display=swap">
<style>
  :root {
    --panel-green: #1a8c02;
    --field-white: #ffffff;
    --accent-orange: #d97b06;
    --cream: #fdf5d5;
    --cream-deep: #f6e9bd;
    --tan: #c49a5d;
    --gold: #b78a4a;
    --text-light: #ffffff;
    --text-soft: #eaf6e4;
  }
  html, body {
    margin: 0;
    padding: 0;
    overflow: hidden;
  }
  .canvas {
    position: relative;
    width: 1200px;
    height: 749px;
    overflow: hidden;
    background: var(--cream);
    font-family: "Inter", sans-serif;
  }
  .login-panel {
    position: absolute;
    left: 0;
    top: 0;
    width: 489px;
    height: 749px;
    background: var(--panel-green);
    color: var(--text-light);
  }
  .login-title {
    position: absolute;
    top: 98px;
    left: 0;
    width: 478px;
    margin: 0;
    text-align: center;
    font-family: "Montserrat", sans-serif;
    font-weight: 700;
    font-size: 58px;
    letter-spacing: 0.5px;
  }
  .field-label {
    position: absolute;
    left: 75px;
    font-size: 17px;
    font-weight: 400;
  }
  .field-label.email { top: 236px; }
  .field-label.password { top: 341px; left: 77px; }
  .text-field {
    position: absolute;
    left: 75px;
    width: 331px;
    height: 54px;
    background: var(--field-white);
    border-radius: 9px;
  }
  .text-field.email { top: 267px; }
  .text-field.password { top: 372px; }
  .eye-toggle {
    position: absolute;
    right: 12px;
    top: 15px;
  }
  .remember {
    position: absolute;
    left: 75px;
    top: 459px;
    display: flex;
    align-items: center;
    gap: 7px;
    font-size: 14px;
  }
  .login-button {
    position: absolute;
    left: 139px;
    top: 512px;
    width: 216px;
    height: 59px;
    border-radius: 30px;
    background: var(--accent-orange);
    color: var(--text-light);
    font-family: "Montserrat", sans-serif;
    font-weight: 800;
    font-size: 25px;
    line-height: 59px;
    text-align: center;
    letter-spacing: 0.5px;
  }
  .register-line {
    position: absolute;
    top: 648px;
    left: 0;
    width: 489px;
    text-align: center;
    font-size: 19px;
    color: var(--text-soft);
  }
  .register-line a {
    color: var(--text-light);
    text-decoration: underline;
    margin-left: 8px;
  }
  .showcase {
    position: absolute;
    left: 489px;
    top: 0;
  }
</style>
</head>
<body>
<div class="canvas">
  <section class="login-panel">
    <h1 class="login-title">Login</h1>

    <span class="field-label email">Email</span>
    <div class="text-field email"></div>

    <span class="field-label password">Password</span>
    <div class="text-field password">
      <svg class="eye-toggle" width="28" height="24" viewBox="0 0 28 24" aria-hidden="true">
        <path d="M2 12 C7 4 21 4 26 12 C21 20 7 20 2 12 Z" fill="none" stroke="#111" stroke-width="2.6"/>
        <circle cx="14" cy="12" r="4" fill="#111"/>
        <line x1="5" y1="2" x2="23" y2="22" stroke="#fff" stroke-width="5"/>
        <line x1="5" y1="2" x2="23" y2="22" stroke="#111" stroke-width="2.6"/>
      </svg>
    </div>

    <label class="remember">
      <svg width="17" height="17" viewBox="0 0 17 17" aria-hidden="true">
        <rect x="0.5" y="0.5" width="16" height="16" rx="3" fill="#e8e8e8"/>
        <path d="M4 8.8 L7.2 12 L13 5" fill="none" stroke="#1a8c02" stroke-width="2.2"/>
      </svg>
      Remember me
    </label>

    <div class="login-button">LOGIN</div>

    <p class="register-line">Dont have an account?<a href="#">Register</a></p>
  </section>

  <svg class="showcase" width="711" height="749" viewBox="489 0 711 749">
    <defs>
      <linearGradient id="tower-photo" x1="0" y1="0" x2="0" y2="1">
        <stop offset="0" stop-color="#7fa8d6"/>
        <stop offset="0.6" stop-color="#8d7a5e"/>
        <stop offset="1" stop-color="#4a3b2b"/>
      </linearGradient>
      <linearGradient id="screen-photo" x1="0" y1="0" x2="0" y2="1">
        <stop offset="0" stop-color="#6c9ee8"/>
        <stop offset="0.45" stop-color="#d9d2c2"/>
        <stop offset="0.7" stop-color="#4f8a3a"/>
        <stop offset="1" stop-color="#e8e8e6"/>
      </linearGradient>
    </defs>

    <rect x="489" y="0" width="711" height="749" fill="#fdf5d5"/>
    <rect x="489" y="0" width="711" height="749" fill="#f6e9bd" opacity="0.35"
          role="img" aria-label="Faint geometric Islamic pattern background"/>

    <circle cx="648" cy="76" r="33" fill="#c49a5d"/>
    <path d="M660 62 L637 76 L660 90 Z" fill="#fff"/>

    <circle cx="1173" cy="50" r="210" fill="url(#tower-photo)"
            role="img" aria-label="Photo of a clock tower above a mosque at dusk"/>

    <path d="M489 190 A105 105 0 0 1 489 400 Z" fill="#b78a4a" opacity="0.55"
          role="img" aria-label="Gold mandala ornament"/>
    <path d="M1200 595 A135 135 0 0 0 1035 749 L1200 749 Z" fill="#b78a4a" opacity="0.6"
          role="img" aria-label="Gold mandala ornament"/>

    <polygon points="700,250 1193,350 1110,666 670,470" fill="#c9cdd6"
             role="img" aria-label="Stacked preview slide of a mosque screen"/>
    <polygon points="660,220 1165,313 1085,610 625,425" fill="#dfe2e8"
             role="img" aria-label="Stacked preview slide of a mosque screen"/>
    <polygon points="620,187 1147,257 1067,547 583,363" fill="url(#screen-photo)"
             role="img" aria-label="Mosque screen display slide showing prayer time, clock and next prayer over a mosque photo"/>
  </svg>
</div>
</body>
</html>
```